Near future techno-thriller needs a mind blowing book cover design!

The Hollow Tonic is the first in a trilogy of techno thrillers set in a very recognisable near future.

The world is changing. A mass market drug promised to boost intelligence. The world embraced it and soon everyone was a genius, but only for a while. The long term effects crippled the world societies. A select few experience much greater changes, becoming something more than human.

The book paints a Rustcanyon like future, a society on the verge of collapse. The only two known posthumans are fighting an incomprehensible war against each other. Carl Brisket, an old fashioned private investigator who is slowly losing his mental faculties as a result of the Drug, is tasked with capturing one of them.

This is a book that ask the question what we might become in the future, if our intellects expanded to the point where the boundaries of intellect no longer apply.

The winning designer will also be used for the second and third book in the series.

Author's name is "Henrik Ålmgård"

MAIN CHARACTERS
Beyond the meta humans, there are two other main characters. This is the description from the book:

Carl Brisket
Carl Brisket is a private investigator in a world where they are no longer needed.

"FenLo studied the man next to him. Carl was asleep or at least it looked that way – his face always seemed set in a frown. Now that he was relaxed, half lying down in the car seat, he looked so old. FenLo knew he was thirty-six, but looked closer to fifty. His dark hair was turning grey. FenLo had seen photos of Carl in his mid-twenties. He had been quite handsome, making it hard to imagine what could have happened. Now he looked like an ageing movie star that had let himself go."

FenLo
FenLo is an operative for a posthuman interest group. He is an expert hacker and also a skilled stick fighter.

"A single streetlight created a cone of light in the centre of the playground, with everything else dimming into darkness. A young man was sitting on one of the swings, dangling his legs back and forth motionless. Like most people under 25, he had a completely integrated uPalo, and it was obvious he was doing something with it. From the occasional twitches in his fingers, Carl guessed he was playing a game. Carl approached him slowly, wondering if he’d come to the right place. As he got closer, he no longer had any doubts. The boy was of Asian descent and the spitting image of his father. He wore baggy pants and a black hoodie with a swirling pattern emanating from the chest. Expensive clothes designed to imitate what actual street kids wore. Carl hated the pretence.
As the more integrated systems almost completely disconnected you from what was going on around you, the uPalo allowed greetings that interrupted the current activity. Carl never had much time for such niceties. He walked up to the pretend gangster and tapped him on the forehead. The young man jolted backwards, tangled up in the swing and fell in a heap."

PROBABILITY MATRIX
One of the core concepts in the book is the idea of a probability matrix available to the posthumans. A mind map of decisions and probabilities. This concept would be interesting to see as the basis for the cover, or maybe the background, with a figure (either a posthuman or the private investigator) in the foreground. Here is a description from the book:

“Is this death?” Carl thought, his mind suspended in darkness.
A single light far away caught his attention. Was this the tunnel of light so common in near-death experiences? He focused on the light and willed himself to move towards it.
Nothing happened. He remained where he was as another light and then another appeared. At first they seemed random, but as they multiplied, thin strands of light connected them until what looked like a major city seen from above at night spread out below him.
It reminded him of the mind maps he could see when he was on the Drug, except much more complex. He no longer tried to move. He knew he was the centre of this space - everything else would move. He willed the map to take him to the beginning, that solitary spot he had first seen.
The dot represented his birth. All light surrounding him represented actions or decisions affecting him. Lines of varying colours and intensity led from this single dot to others, representing the probability.
He wanted to remain here to explore, but a distant pulsating light drew his attention. He travelled forward to now and studied the end of his life. To his surprise it didn’t end. From the current time there was a decision point with only a ten percent likelihood of death. The outgoing lines suggested many options. One in particular interested him as it had a high probability and included a line that seemed to depart from the matrix altogether. He followed it and a new matrix opened. This time the nodes were no longer decision points in his life. They were codes that translated to locations, people and devices as he studied them. It was a network diagram based on what he could access….

POSTHUMANS
Another core concept is the postHumans. They are people who has had their minds enhanced by the drug, but this is just the starting point. In the book one of the postHumans become a distributed mind, across multiple bodies. Another starts reconfiguring their body. Below are two sections from the book detailing this:

"Marva had made a remarkable recovery. Her skin had regenerated, shedding the old burnt one like sunburnt skin. The new skin was harder, more akin to a reptile’s, which made even taking blood samples difficult. Not that he knew what to do with them any longer, anyway. Most of her bodily processes had changed. She was still human, but only in the same sense that a Velocar Prime car was a car. He suspected this was not a direct result of CereVox, but only a follow-on effect. The Drug had opened the door, but Marva was the architect behind the modifications, whether consciously or unconsciously. She had been killed, but managed to keep her body in a suspended state until the base functions could repair themselves and harden her body for any future attacks."

"My subconscious had begun a reconfiguration of what I was – a body to match the intellect it housed. It hadn’t even occurred to me until now that I could examine my body and its automatic processes in much the same as I could examine anything else.
What a marvelous machine it is, and yet so flawed.
It took only a cursory examination to question the possible involvement of a creator in its design. The mystery – if there was one – was how we had progressed this far at all. The spine was a prime example. It was an amazing construction for movement, but was obviously not for walking upright. Mine was reinforced, limiting movement somewhat. This was an understandable trade-off. Most of my physical enhancements, I discovered, were to better protect the brain and basic movement whilst limiting agility somewhat.
As I studied the different layers of the body, I found adjustments everywhere.
My metabolism had changed. I was now a hybrid with an organ specifically designed to store energy to feed my ever-increasing mind. Instead of allowing high-energy food such as sugars to flood my system, it stored them like a battery and released them as needed.
I had already seen the difference in analytics and critical thinking. The brain is an amazing organ, but to deal with the constant barrage of data and make sense of it, it filters, fills in the blanks and makes assumptions. My brain no longer did this. Instead it processed all information, made all the necessary connections and fed the result into the probability matrix.
The most surprising changes I found were in the building blocks of who I was. A completely new process was reprogramming my genome using designed viruses as the tool. A new organ created viruses and released them into the body. It changed the cell by infecting it, reprogramming all the cells in my body continuously. It was correcting deficiencies in my DNA."

Target Market(s)

From a cover perspective the book needs to capture readers who like near future sci-fi and techno thrillers. Here are some examples that have the right idea, but maybe slightly cheap looking approach:

http://www.pelmarobooks.com.au/The-Ember-Mind-Vantage-Series-ebook/dp/K47QX2MZRT/ref=pd_sim_351_2?ie=UTF8&refRID=5H2KP8LMQ3RTZWX4NB7C

http://www.pelmarobooks.com.au/drift-Tallow-Meridian-Book-ebook/dp/K39VW8RTYP/ref=pd_sim_351_2?ie=UTF8&refRID=6Q8DZ3HJT5MXCL2PVA09

Here is another that has similar themes:

http://www.pelmarobooks.com.au/Quorra-The-Trilogy-Book-ebook/dp/K52LHX4NWQ/ref=pd_sim_351_2?ie=UTF8&refRID=2D7FK9MBRS4JTUE6YHAL

Industry/Entity Type

Drug

Requirements
Must have
• This is an eBook cover for a kindle. I also need a standard sized cover with spine and back cover. The back cover blurb:
• “You may wonder why I tell you this, but bear with me. I didn’t realize it then, but I had stumbled on something of enormous importance. Something that will redefine mankind. Something that could redefine you.”
• Lucian – postHuman
• The world is changing. A mass market drug promised to boost intelligence. The world embraced it and soon everyone was a genius, but only for a while. The long term effects crippled the world societies. A select few experience much greater changes, becoming something more than human.
• Carl Brisket is hired by the very medical company that introduced the drug in the first place, to capture one of the posthumans. He finds himself part of a new world rising from the ashes of the old.
• The Hollow Tonic is a scif-fi thriller set in a very recognisable near future.

```html
<!DOCTYPE html>
<html lang="en">
<head>
<meta charset="utf-8">
<title>The Hollow Tonic — Full Cover</title>
<link rel="stylesheet" href="https://fonts.googleapis.com/css2?family=Tinos&family=Oswald:wght@400&display=swap">
<style>
  :root{
    --navy-deep:#06143a;
    --navy:#0d2a66;
    --blue:#1f4f9c;
    --blue-glow:#4f86cf;
    --ice:#a9c6ee;
    --text:#ffffff;
    --pill-red:#c8141b;
    --pill-white:#f4f4f4;
  }
  *{margin:0;padding:0;box-sizing:border-box}
  html,body{width:1200px;height:855px;overflow:hidden;background:var(--navy-deep)}
  .cover{
    position:relative;width:1200px;height:855px;overflow:hidden;
    background:
      radial-gradient(ellipse 520px 420px at 300px 430px, rgba(79,134,207,.35), transparent 70%),
      linear-gradient(135deg, var(--navy) 0%, var(--navy-deep) 45%, var(--navy) 75%, var(--blue) 100%);
    color:var(--text);
    font-family:"Tinos", "Times New Roman", serif;
  }
  .hero-art{
    position:absolute;left:600px;top:0;width:600px;height:600px;
    background:
      radial-gradient(ellipse 230px 300px at 420px 230px, rgba(169,198,238,.55), transparent 70%),
      radial-gradient(ellipse 300px 260px at 230px 200px, rgba(79,134,207,.45), transparent 70%);
  }
  .back-title,.front-title{
    font-weight:400;text-align:center;line-height:.9;letter-spacing:1px;white-space:nowrap;
  }
  .back-title{position:absolute;left:60px;top:58px;width:460px;font-size:62px}
  .blurb{
    position:absolute;left:68px;top:232px;width:434px;
    font-size:15.5px;line-height:27.5px;text-align:justify;
  }
  .blurb p{margin-bottom:27.5px}
  .blurb .attribution{margin-top:-27.5px}
  .spine{
    position:absolute;left:561px;top:0;width:52px;height:855px;
    background:linear-gradient(90deg, rgba(6,20,58,.5), rgba(6,20,58,.25));
  }
  .spine-title,.spine-author{
    position:absolute;left:50%;transform:translateX(-50%);
    writing-mode:vertical-rl;white-space:nowrap;
  }
  .spine-title{top:42px;font-size:37px;letter-spacing:1px}
  .spine-author{top:470px;font-family:"Oswald", "Arial Narrow", sans-serif;font-size:34px;letter-spacing:2px}
  .front-title{position:absolute;left:620px;top:468px;width:575px;font-size:78px}
  .pill{position:absolute;left:839px;top:683px}
  .front-author{
    position:absolute;left:620px;top:764px;width:575px;text-align:center;
    font-family:"Oswald", "Arial Narrow", sans-serif;font-size:50px;letter-spacing:2px;line-height:1;
  }
</style>
</head>
<body>
<div class="cover">
  <div class="hero-art" role="img" aria-label="Illustration of a shattering blue digital human head in profile over circuit-board lines"></div>

  <section class="back-cover">
    <h2 class="back-title">THE HOLLOW<br>TONIC</h2>
    <div class="blurb">
      <p>“You may wonder why I tell you this, but bear with me. I didn’t realize it then, but I had stumbled on something of enormous importance. Something that will redefine mankind. Something that could redefine you.”</p>
      <p class="attribution">Lucian - postHuman</p>
      <p>The world is changing. A mass market drug promised to boost intelligence. The world embraced it and soon everyone was a genius, but only for a while. The long term effects crippled the world societies. A select few experience much greater changes, becoming something more than human.</p>
      <p>Carl Brisket is hired by the very medical company that introduced the drug in the first place, to capture one of the posthumans. He finds himself part of a new world rising from the ashes of the old.</p>
      <p>The Hollow Tonic is a scif-fi thriller set in a very recognisable near future.</p>
    </div>
  </section>

  <section class="spine">
    <div class="spine-title">THE HOLLOW TONIC</div>
    <div class="spine-author">HENRIK ÅLMGÅRD</div>
  </section>

  <section class="front-cover">
    <h1 class="front-title">THE HOLLOW<br>TONIC</h1>
    <svg class="pill" width="142" height="40" viewBox="0 0 142 40" aria-hidden="true">
      <defs>
        <linearGradient id="pillShade" x1="0" y1="0" x2="0" y2="1">
          <stop offset="0" stop-color="#fff" stop-opacity=".45"/>
          <stop offset=".5" stop-color="#fff" stop-opacity="0"/>
          <stop offset="1" stop-color="#000" stop-opacity=".25"/>
        </linearGradient>
      </defs>
      <path d="M20 1 H71 V39 H20 A19 19 0 0 1 20 1 Z" fill="var(--pill-red)"/>
      <path d="M71 1 H122 A19 19 0 0 1 122 39 H71 Z" fill="var(--pill-white)"/>
      <rect x="1" y="1" width="140" height="38" rx="19" fill="url(#pillShade)"/>
    </svg>
    <div class="front-author">HENRIK ÅLMGÅRD</div>
  </section>
</div>
</body>
</html>
```